Guaranteed Job - Sleek Sexy Business Card UV Spot

Im looking for a sleek and sexy business card, that resembles elite or VIP status status.
our business is corinvale.example
you can view our products on there, but our main audience for handing out our cards will be for people in the hospitality industry, so it will need to impress high management and CEO of hotels and restaurants, bars, clubs etc...
the card features will have UV spot on both sides, 400gsm stock. standard size.
Artwork should be 86 x 54mm + 2mm bleed = 90 x 58mm
it should have a nice "unique" uv spot pattern that highlights the card, not a repeated pattern, theres no originality there, and it will be disregarded.
The written material will be:
Corin Vale Hospitality College (logo)
Tobin Marsh
Director
Phone: 1300 615 737
Mobile: 0455 817 296
Email: info@corinvale.example
website: www.corinvale.example
I'm looking for originality here, i don't want just a simple stock card, want something that has a wow factor for people.
You will find the logo attached. you may invert the white to black words to suit the background as you please.
thank you and good luck
As a side note, ive received a lot of proposals, im too busy to give feedback to each and every one, so if i havent provided feedback for your design within 24 hours, then consider it not acceptable, and you could resubmit another design.
So far i have not seen any design that stood out for me, they all seem pretty generic. there nothing thats unique, i would figure for the amount that im offering, that people would put some more effort and creativity into the design.
so far over 200 designs submitted, and nothing i have seen looks very original, everything looks like a different variation of the same stuff, i said it very clearly i wanted something unique, the only thing that has come close to it so far is this one
Reason: Ive received alot of design concepts and i have reviewed everyone, but i havent had time to give feedback to every single one, only the ones that have interested me, if i havent responded, its because i havent found it good enough.
so far only a few design have been on par with what ive been looking for, an attractive eye popping design.
heres a few of them,
http://files.pixelbazaar.example/design_img/51736/62418/62418_2840915_51736_image.jpg
http://files.pixelbazaar.example/design_img/51736/68254/68254_2841377_51736_image.jpg
theyre, both unique and original, and eye catching, the only thing theyre missing is the sexyness.
if you still think you have some creativity left in your minds, then throw it on here.
Reason: Sorry guys for the delay, I was in a serious accident and out of commission for the past few months, I'm just slowly recovering now, please bare with me as i try to attend to this project, it may take me awhile as I have other projects that are on standby, I'm not 100% at the moment, so im extending the deadline for 2 weeks right now. Thanks for your patience.
Hospitality

```html
<!DOCTYPE html>
<html lang="en">
<head>
<meta charset="utf-8">
<title>Corin Vale Hospitality College – Business Card Options</title>
<link rel="stylesheet" href="https://fonts.googleapis.com/css2?family=Arimo:wght@400&family=Kaushan+Script&family=Open+Sans:wght@400;600;700&display=swap">
<style>
  :root {
    --blue: #0f7fd2;
    --offwhite: #f8f3cf;
    --ink: #111111;
    --band: #c4c4c4;
    --trim: #e4656a;
    --rule: #222222;
    --card-black: #050505;
    --faint-grey: #2b2b2b;
  }
  * { margin: 0; padding: 0; box-sizing: border-box; }
  html, body { width: 1200px; height: 1129px; overflow: hidden; background: #ffffff; }
  .sheet {
    position: relative; width: 1117px; height: 1050px;
    transform: scale(1.0743); transform-origin: 0 0;
    font-family: "Open Sans", Arial, sans-serif; color: var(--ink);
  }
  .option-label, .spec, .note, .dimension-label {
    position: absolute; font-family: "Arimo", Arial, sans-serif; color: var(--ink);
  }
  .option-label { font-size: 14px; letter-spacing: .3px; transform: translateX(-50%); }
  .spec { font-size: 22px; line-height: 30px; }
  .note { font-size: 24px; }
  .dimension-label { font-size: 14px; }
  .divider { position: absolute; left: 5px; width: 1095px; height: 0; border: 0; border-top: 1.5px solid var(--rule); }
  .dimension { position: absolute; }

  .card {
    position: absolute; width: 341px; height: 219px; background: #fff;
    border: 1px solid var(--trim); overflow: hidden;
  }
  .card--rounded { border-radius: 14px; }
  .card--black { background: var(--card-black); }
  .card--folded { height: 188px; overflow: visible; }

  .brand { position: absolute; display: flex; align-items: center; gap: 10px; color: var(--blue); font-weight: 700; z-index: 1; }
  .brand-mark { width: 40px; height: 40px; background: var(--blue); flex: none; }
  .brand-name { line-height: 1; text-transform: uppercase; font-size: 19px; }
  .brand-name small { display: block; font-size: 8px; letter-spacing: .6px; margin-top: 4px; }

  .signature { position: absolute; font-family: "Kaushan Script", cursive; font-size: 15px; color: var(--ink); white-space: nowrap; }
  .role { position: absolute; font-size: 9px; color: var(--ink); }
  .contact-list { position: absolute; list-style: none; font-size: 8.6px; font-weight: 600; line-height: 11.3px; text-align: right; }
  .hairline { position: absolute; height: 0; border-top: 1px solid #bbbbbb; }
  .hairline--blue { border-top-color: var(--blue); }

  .lettered-list { position: absolute; list-style: none; font-size: 9px; line-height: 15px; z-index: 1; }
  .lettered-list li { display: flex; align-items: center; gap: 9px; }
  .letter-chip { width: 12px; height: 12px; background: var(--offwhite); color: var(--blue); font-weight: 700; font-size: 8px; display: grid; place-items: center; }

  .uv-artwork {
    position: absolute; left: 178px; top: 0; width: 163px; height: 219px;
    background: linear-gradient(135deg, #ffffff 0%, var(--offwhite) 45%, #3a3a3a 100%);
  }

  .rule-grey { position: absolute; left: 0; width: 100%; border-top: 1px solid #555; }
  .holder-name { position: absolute; width: 100%; text-align: center; font-weight: 700; z-index: 1; }
  .holder-name--blue { color: var(--blue); font-size: 16px; }
  .holder-role--blue { position: absolute; width: 100%; text-align: center; color: var(--blue); font-size: 9px; }
  .marker { position: absolute; width: 0; height: 0; border-top: 4px solid transparent; border-bottom: 4px solid transparent; }
  .marker--right { border-left: 7px solid #fff; }
  .marker--left { border-right: 7px solid #fff; }
  .icon-row { position: absolute; display: flex; gap: 4px; align-items: center; font-size: 9px; white-space: nowrap; z-index: 1; }
  .icon-row svg { width: 10px; height: 10px; flex: none; }
  .icon-row--blue { color: var(--blue); }
  .icon-row--blue svg { fill: var(--blue); }
  .faint-square { position: absolute; left: 300px; top: 120px; width: 80px; height: 80px; background: var(--faint-grey); transform: rotate(-30deg); }

  .holder-name--dark { font-size: 16px; width: auto; text-align: right; }
  .band { position: absolute; left: 0; top: 0; }
  .fold-text { position: absolute; left: 70px; top: 188px; font-size: 5px; color: #777; white-space: nowrap; }
</style>
</head>
<body>
<svg width="0" height="0" style="position:absolute" aria-hidden="true">
  <symbol id="icon-phone" viewBox="0 0 10 10"><rect width="10" height="10" rx="1"/><path d="M3 2.2c.4 0 .8 1 .8 1.4 0 .3-.5.5-.4.8.3.8 1 1.5 1.8 1.8.3.1.5-.4.8-.4.4 0 1.4.4 1.4.8 0 .6-.7 1.2-1.3 1.2C4.3 7.8 2.2 5.7 2.2 3.5c0-.6.4-1.3.8-1.3z" fill="#fff"/></symbol>
  <symbol id="icon-mobile" viewBox="0 0 10 10"><rect x="2" width="6" height="10" rx="1"/><rect x="3" y="1.3" width="4" height="6" fill="#fff"/></symbol>
  <symbol id="icon-mail" viewBox="0 0 10 10"><rect width="10" height="10" rx="1"/><rect x="1.8" y="3" width="6.4" height="4.2" fill="#fff"/><path d="M1.8 3 5 5.5 8.2 3" stroke="#000" stroke-width=".7" fill="none"/></symbol>
  <symbol id="icon-web" viewBox="0 0 10 10"><rect width="10" height="10" rx="1"/><circle cx="5" cy="5" r="3.2" fill="none" stroke="#fff" stroke-width=".8"/><path d="M1.8 5h6.4M5 1.8v6.4" stroke="#fff" stroke-width=".7"/></symbol>
</svg>

<main class="sheet">
  <span class="option-label" style="left:240px;top:3px">OPTION # 1</span>
  <span class="option-label" style="left:615px;top:3px">OPTION # 2</span>

  <span class="dimension-label" style="left:218px;top:38px">90mm</span>
  <svg class="dimension" style="left:66px;top:62px" width="348" height="14" aria-hidden="true">
    <line x1="3" y1="6" x2="345" y2="6" stroke="#555" stroke-width="1"/>
    <line x1="3" y1="0" x2="3" y2="14" stroke="#555"/><line x1="345" y1="0" x2="345" y2="14" stroke="#555"/>
  </svg>
  <span class="dimension-label" style="left:2px;top:178px">58mm</span>
  <svg class="dimension" style="left:40px;top:82px" width="14" height="222" aria-hidden="true">
    <line x1="7" y1="2" x2="7" y2="220" stroke="#555"/>
    <line x1="0" y1="2" x2="14" y2="2" stroke="#555"/><line x1="0" y1="220" x2="14" y2="220" stroke="#555"/>
  </svg>

  <section class="card" style="left:69px;top:83px" aria-label="Option 1 card">
    <div class="brand" style="left:12px;top:40px">
      <span class="brand-mark"></span>
      <span class="brand-name">Corin<br>Vale<small>Hospitality College</small></span>
    </div>
    <span class="signature" style="right:10px;top:124px">Tobin Marsh</span>
    <span class="role" style="right:16px;top:144px">Director</span>
    <span class="hairline" style="left:178px;right:12px;top:158px"></span>
    <ul class="contact-list" style="right:12px;top:164px">
      <li>Phone: 1300 615 737</li>
      <li>Mobile: 0455 817 296</li>
      <li>Email: info@corinvale.example</li>
      <li>website: www.corinvale.example</li>
    </ul>
  </section>

  <section class="card" style="left:444px;top:83px" aria-label="Option 2 card">
    <div class="brand" style="left:20px;top:48px;flex-direction:column;align-items:flex-start;gap:8px">
      <span class="brand-mark"></span>
      <span class="brand-name">Corin<br>Vale<small>Hospitality College</small></span>
    </div>
    <span class="signature" style="right:20px;top:84px">Tobin Marsh</span>
    <span class="role" style="right:22px;top:104px">Director</span>
    <span class="hairline hairline--blue" style="left:168px;right:20px;top:118px"></span>
    <ul class="contact-list" style="right:22px;top:124px">
      <li>Phone: 1300 615 737</li>
      <li>Mobile: 0455 817 296</li>
      <li>Email: info@corinvale.example</li>
      <li>website: www.corinvale.example</li>
    </ul>
  </section>

  <p class="spec" style="left:806px;top:145px">White Background<br>Blue &amp; Black Metter Color<br>Offwhite Color For Spot UV</p>
  <p class="note" style="left:70px;top:319px">Offwhite Color For Spot UV</p>

  <hr class="divider" style="top:367px">

  <span class="option-label" style="left:240px;top:395px">OPTION # 3</span>
  <span class="option-label" style="left:615px;top:395px">OPTION # 4</span>

  <section class="card card--rounded" style="left:69px;top:420px" aria-label="Option 3 card">
    <div class="uv-artwork" role="img" aria-label="Spot UV artwork area: sweeping offwhite and black strokes"></div>
    <div class="brand" style="left:12px;top:30px">
      <span class="brand-mark"></span>
      <span class="brand-name">Corin<br>Vale<small>Hospitality College</small></span>
    </div>
    <span class="signature" style="left:10px;top:103px">Tobin Marsh</span>
    <span class="role" style="left:12px;top:124px">Director</span>
    <ul class="lettered-list" style="left:14px;top:142px">
      <li><span class="letter-chip">P</span>1300 615 737</li>
      <li><span class="letter-chip">M</span>0455 817 296</li>
      <li><span class="letter-chip">E</span>info@corinvale.example</li>
      <li><span class="letter-chip">W</span>www.corinvale.example</li>
    </ul>
  </section>

  <section class="card card--black" style="left:444px;top:420px;color:#fff" aria-label="Option 4 card">
    <span class="faint-square" aria-hidden="true"></span>
    <div class="brand" style="left:86px;top:18px">
      <span class="brand-mark"></span>
      <span class="brand-name" style="color:#fff">Corin<br>Vale<small>Hospitality College</small></span>
    </div>
    <span class="rule-grey" style="top:100px"></span>
    <span class="marker marker--right" style="left:92px;top:118px"></span>
    <span class="holder-name holder-name--blue" style="top:110px">Tobin Marsh</span>
    <span class="holder-role--blue" style="top:132px">Director</span>
    <span class="marker marker--left" style="left:242px;top:118px"></span>
    <div class="icon-row icon-row--blue" style="left:40px;top:167px"><svg><use href="#icon-phone"/></svg>1300 615 737</div>
    <div class="icon-row icon-row--blue" style="left:178px;top:167px"><svg><use href="#icon-mobile"/></svg>0455 817 296</div>
    <div class="icon-row icon-row--blue" style="left:40px;top:187px"><svg><use href="#icon-mail"/></svg>info@corinvale.example</div>
    <div class="icon-row icon-row--blue" style="left:178px;top:187px"><svg><use href="#icon-web"/></svg>www.corinvale.example</div>
    <span class="rule-grey" style="top:204px"></span>
  </section>

  <p class="spec" style="left:806px;top:483px">Black Background<br>Blue Metter Color<br>White Color Spot UV</p>
  <p class="note" style="left:95px;top:647px">Offwhite Color For Spot UV</p>

  <hr class="divider" style="top:728px">

  <span class="option-label" style="left:240px;top:744px">OPTION # 5</span>
  <span class="option-label" style="left:615px;top:744px">OPTION # 5</span>

  <section class="card" style="left:58px;top:778px" aria-label="Option 5 card, open">
    <svg class="band" width="341" height="219" viewBox="0 0 341 219" aria-hidden="true">
      <polygon points="128,166 341,166 341,189 128,189 150,178" fill="var(--band)"/>
      <rect x="0" y="190" width="341" height="29" fill="var(--band)"/>
      <line x1="0" y1="192" x2="341" y2="192" stroke="#777" stroke-dasharray="3 2" stroke-width=".7"/>
      <polyline points="0,166 22,178 0,190" fill="none" stroke="var(--trim)"/>
    </svg>
    <div class="brand" style="left:92px;top:22px">
      <span class="brand-mark"></span>
      <span class="brand-name">Corin<br>Vale<small>Hospitality College</small></span>
    </div>
    <span class="holder-name holder-name--dark" style="right:30px;top:116px">Tobin Marsh</span>
    <span class="role" style="right:60px;top:138px">Director</span>
    <div class="icon-row" style="left:166px;top:172px"><svg><use href="#icon-phone"/></svg>1300 615 737</div>
    <div class="icon-row" style="left:250px;top:172px"><svg><use href="#icon-mobile"/></svg>0455 817 296</div>
    <div class="icon-row" style="left:60px;top:201px"><svg><use href="#icon-mail"/></svg>info@corinvale.example</div>
    <div class="icon-row" style="left:198px;top:201px"><svg><use href="#icon-web"/></svg>www.corinvale.example</div>
  </section>

  <section class="card card--folded" style="left:443px;top:778px" aria-label="Option 5 card, folded">
    <svg class="band" width="343" height="202" viewBox="0 0 343 202" aria-hidden="true">
      <polygon points="128,166 341,166 341,187 128,187 150,177" fill="var(--band)"/>
      <polyline points="0,166 22,177 0,188" fill="none" stroke="var(--trim)"/>
      <rect x="0" y="188" width="343" height="10" fill="#e6e6e6"/>
      <line x1="0" y1="198" x2="343" y2="198" stroke="var(--trim)" stroke-dasharray="3 2" stroke-width=".7"/>
    </svg>
    <span class="fold-text">info@corinvale.example &nbsp;&nbsp;&nbsp; www.corinvale.example</span>
    <div class="brand" style="left:92px;top:22px">
      <span class="brand-mark"></span>
      <span class="brand-name">Corin<br>Vale<small>Hospitality College</small></span>
    </div>
    <span class="holder-name holder-name--dark" style="right:30px;top:116px">Tobin Marsh</span>
    <span class="role" style="right:60px;top:138px">Director</span>
    <div class="icon-row" style="left:166px;top:171px"><svg><use href="#icon-phone"/></svg>1300 615 737</div>
    <div class="icon-row" style="left:250px;top:171px"><svg><use href="#icon-mobile"/></svg>0455 817 296</div>
  </section>

  <p class="spec" style="left:806px;top:832px">Size: 90mm x 58mm<br>DIE Cutting &amp; Folding<br>For Dami</p>
  <p class="note" style="left:85px;top:1014px">Offwhite Color For Spot UV</p>
</main>
</body>
</html>
```